Kestrelway Advisory logo/business card design -- a digital consulting company

I've just restarted a consulting company I had years ago--Kestrelway Advisory. Now I need a new business card and updated logo. The original logo was simple enough: a chart-like progression atop a grid (see the attached file). I do strategy work, and the chart is meant to show incremental growth and profit. I'd like the reincarnation of my logo to be 3D, with both the grid and arrow rotated on their axis.

I'll want to use the logo on my website as well. I'm open to color schemes, fonts, etc.

Target Market(s)

Business-to-Business. Target market is corporate.

Industry/Entity Type

Business

Contact Information for Business Card

Logo on one-side; name and other contact info on the back

Font styles to use
Serif
Sans Serif

Requirements
Nice to have
• Kestrelway Advisory refers to the concept of "bootstrapping" or making incremental changes to grow with minimal risk and financial exposure, and self-sufficiency (think of the phrase "to pull oneself by one's bootstraps.")

```html
<!DOCTYPE html>
<html lang="en">
<head>
<meta charset="utf-8">
<title>Kestrelway Advisory – Business Card</title>
<link rel="stylesheet" href="https://fonts.googleapis.com/css2?family=Didact+Gothic&family=Montserrat:wght@600;700&display=swap">
<style>
  :root {
    --stage: #2b2b2d;
    --card-dark-top: #3b4350;
    --card-dark-bottom: #272c35;
    --card-light: #f4f4f2;
    --brand-red: #e0232c;
    --ink-light: #f2f3f5;
    --ink-grey: #6d6f73;
    --divider: rgba(255,255,255,0.28);
  }
  * { margin: 0; padding: 0; box-sizing: border-box; }
  html, body {
    width: 1200px; height: 900px; overflow: hidden;
    background: var(--stage);
  }
  .stage {
    position: relative; width: 1200px; height: 900px;
    display: flex; flex-direction: column; align-items: center;
    justify-content: center; gap: 46px;
  }
  .card {
    width: 640px; height: 366px; border-radius: 4px;
    box-shadow: 0 14px 30px rgba(0,0,0,0.45);
    position: relative;
  }
  /* Back: contact side */
  .card--back {
    background: linear-gradient(160deg, var(--card-dark-top), var(--card-dark-bottom));
    display: flex; align-items: center;
    font-family: "Didact Gothic", sans-serif;
  }
  .holder {
    width: 300px; padding-right: 28px; text-align: right;
  }
  .holder__name {
    font-family: "Montserrat", sans-serif; font-weight: 700;
    color: var(--brand-red); font-size: 27px; letter-spacing: 0.2px;
  }
  .holder__role {
    color: var(--ink-light); font-size: 15px; margin-top: 2px;
  }
  .divider {
    width: 1px; height: 140px;
    background: linear-gradient(to bottom, transparent, var(--divider), transparent);
  }
  .contact {
    padding-left: 36px; color: var(--ink-light); font-size: 14px; line-height: 1.35;
  }
  .contact__address { margin-bottom: 12px; }
  .contact__row { display: flex; align-items: center; gap: 9px; }
  .contact__icon { width: 11px; height: 11px; flex: none; }

  /* Front: name side */
  .card--front {
    background: var(--card-light);
    display: flex; flex-direction: column; align-items: center; justify-content: center;
    font-family: "Montserrat", sans-serif;
  }
  .brand {
    display: flex; align-items: center; gap: 14px;
  }
  .brand__mark {
    width: 22px; height: 22px; border-radius: 50%; background: var(--brand-red);
  }
  .brand__name {
    font-weight: 700; font-size: 40px; color: var(--brand-red); letter-spacing: 0.5px;
  }
  .brand__rule {
    margin-top: 16px; width: 300px; height: 1px; background: var(--ink-grey);
  }
</style>
</head>
<body>
<main class="stage">
  <section class="card card--back" aria-label="Card back with contact details">
    <div class="holder">
      <p class="holder__name">Dana Whitfield</p>
      <p class="holder__role">Director</p>
    </div>
    <div class="divider"></div>
    <div class="contact">
      <p class="contact__address">000 Harrow Lane<br>Eastfield Park, dummy, 0000</p>
      <p class="contact__row">
        <svg class="contact__icon" viewBox="0 0 12 12"><path d="M2.5 1 L4.5 1 L5.2 3.6 L4 4.6 Q5 7 7.4 8 L8.4 6.8 L11 7.5 L11 9.5 Q10 11 8.5 11 Q1 9 1 2.5 Q1.2 1.2 2.5 1 Z" fill="var(--brand-red)"/></svg>
        0123 456 789
      </p>
      <p class="contact__row">
        <svg class="contact__icon" viewBox="0 0 12 12"><rect x="0.5" y="2.5" width="11" height="7.5" rx="1" fill="var(--brand-red)"/><path d="M0.8 3 L6 7 L11.2 3" stroke="#2b313b" stroke-width="1" fill="none"/></svg>
        dana@kestrelwayadvisory.com
      </p>
      <p class="contact__row">
        <svg class="contact__icon" viewBox="0 0 12 12"><circle cx="6" cy="6" r="5.5" fill="var(--brand-red)"/><path d="M0.5 6 H11.5 M6 0.5 Q2.5 6 6 11.5 M6 0.5 Q9.5 6 6 11.5" stroke="#2b313b" stroke-width="0.8" fill="none"/></svg>
        www.kestrelwayadvisory.com
      </p>
    </div>
  </section>

  <section class="card card--front" aria-label="Card front with company name">
    <div class="brand">
      <span class="brand__mark"></span>
      <p class="brand__name">Kestrelway Advisory</p>
    </div>
    <div class="brand__rule"></div>
  </section>
</main>
</body>
</html>
```